New business card design

I need original, modern, business looking but dzen (minimalistic) looking design.
Also refer to websit trevanix.ru

Text is

Дробышев Кирилл, PMP
Партнер

Моб. +7 (915) 460 7185
info@trevanix.ru
Москва, Россия, 117342, ул. Береговая 7/2
=====================

Drobyshev Kirill, PMP
Partner

Mob. +7 (915) 460 7185
info@trevanix.ru
Moscow, Russia,117342, Beregovaya 7/2

Industry/Entity Type

Business

Font styles to use
Serif
Sans Serif

```html
<!DOCTYPE html>
<html lang="en">
<head>
<meta charset="utf-8">
<title>Trevanix — business card</title>
<link href="https://fonts.googleapis.com/css2?family=Arimo:wght@400;700&display=swap" rel="stylesheet">
<style>
  :root {
    --backdrop: #e9ecee;
    --card: #ffffff;
    --cyan: #1fb6d9;
    --ink: #1d1d1f;
    --muted: #2b2b2b;
    --shadow: rgba(0, 0, 0, 0.12);
  }
  * { box-sizing: border-box; margin: 0; padding: 0; }
  html, body {
    width: 1200px;
    height: 750px;
    overflow: hidden;
    background: var(--backdrop);
    font-family: "Arimo", Arial, sans-serif;
    color: var(--ink);
  }
  .canvas {
    width: 1200px;
    height: 750px;
    display: flex;
    align-items: center;
    justify-content: center;
    gap: 40px;
  }
  .card {
    position: relative;
    width: 540px;
    height: 310px;
    background: var(--card);
    box-shadow: 0 8px 24px var(--shadow);
    overflow: hidden;
  }

  /* brand name */
  .brand {
    display: flex;
    align-items: center;
    gap: 16px;
    position: absolute;
  }
  .brand-mark {
    width: 44px;
    height: 44px;
    background: var(--cyan);
  }
  .brand-name {
    font-weight: 400;
    color: var(--ink);
    letter-spacing: 0.5px;
    line-height: 1;
  }

  /* front side */
  .front .brand { left: 44px; top: 40px; }
  .front .brand-name { font-size: 58px; }
  .holder {
    position: absolute;
    left: 44px;
    top: 170px;
  }
  .holder-name {
    font-size: 18px;
    font-weight: 700;
    color: var(--cyan);
  }
  .holder-role {
    margin-top: 10px;
    font-size: 16px;
    font-weight: 700;
    color: var(--ink);
    text-align: right;
  }
  .contacts {
    position: absolute;
    left: 290px;
    top: 166px;
    list-style: none;
    font-size: 14px;
    color: var(--muted);
  }
  .contacts li {
    display: flex;
    align-items: flex-start;
    gap: 12px;
    margin-bottom: 12px;
    line-height: 1.3;
  }
  .contacts svg {
    flex: none;
    width: 18px;
    height: 18px;
    margin-top: 1px;
    fill: var(--cyan);
  }

  /* back side */
  .back .brand { left: 44px; top: 36px; }
  .back .brand-name { font-size: 76px; }
  .back .brand-mark { width: 56px; height: 56px; }
  .band {
    position: absolute;
    left: 0;
    right: 0;
    top: 176px;
    height: 34px;
    background: var(--cyan);
    display: flex;
    align-items: center;
    padding-left: 44px;
  }
  .site {
    font-size: 16px;
    font-weight: 700;
    color: var(--ink);
  }
</style>
</head>
<body>
<main class="canvas">

  <section class="card front" aria-label="Card front">
    <div class="brand">
      <span class="brand-mark"></span>
      <span class="brand-name">Trevanix</span>
    </div>

    <div class="holder">
      <p class="holder-name">Drobyshev Kirill, PMP</p>
      <p class="holder-role">Partner</p>
    </div>

    <ul class="contacts">
      <li>
        <svg viewBox="0 0 24 24" aria-hidden="true"><path d="M12 2a7 7 0 0 0-7 7c0 5 7 13 7 13s7-8 7-13a7 7 0 0 0-7-7zm0 9.5A2.5 2.5 0 1 1 12 6.5a2.5 2.5 0 0 1 0 5z"/></svg>
        <span>Beregovaya 7/2<br>Moscow, Russia, 117342</span>
      </li>
      <li>
        <svg viewBox="0 0 24 24" aria-hidden="true"><path d="M6.6 10.8a15.1 15.1 0 0 0 6.6 6.6l2.2-2.2a1 1 0 0 1 1-.25 11.4 11.4 0 0 0 3.6.57 1 1 0 0 1 1 1V20a1 1 0 0 1-1 1A17 17 0 0 1 3 4a1 1 0 0 1 1-1h3.5a1 1 0 0 1 1 1c0 1.25.2 2.45.57 3.6a1 1 0 0 1-.25 1z"/></svg>
        <span>+7 (915) 460 7185</span>
      </li>
      <li>
        <svg viewBox="0 0 24 24" aria-hidden="true"><path d="M2 5h20v14H2zm2 2v.5l8 5 8-5V7l-8 5z"/></svg>
        <span>info@trevanix.ru</span>
      </li>
    </ul>
  </section>

  <section class="card back" aria-label="Card back">
    <div class="band"><span class="site">www.trevanix.ru</span></div>
    <div class="brand" style="top:210px; left:auto; right:40px;">
      <span class="brand-name">Trevanix</span>
    </div>
    <div class="brand">
      <span class="brand-mark"></span>
    </div>
  </section>

</main>
</body>
</html>
```